Business Card Design

We are starting up a new Family run Business mainly offering a Free House Clearance service. We also offer the following chargeable services which include a Removals Service, Delivery and Collection of Items sold or purchased on Bidloft, Swapwren etc, including Motorcycles, Piano's, Furniture, Electrical appliances.
As there are a few Companies offering similar services we need to stand out and show what we do at a glance while appearing Professional and approachable
Updates

TidyNests

i  am liking some of the colours and designs so far but would like to see a few of our services listed as 1 or 2 have already done if this is possible and maybe some emphasis on the FREE House Clearance. thank you 
best regards
derek

Target Market(s)

Commercial and Domestic Tenants and Landlords aswell as Families looking for a friendly sympathetic clearance service after bereavement

Industry/Entity Type

Business

Contact Information for Business Card

TidyNests,
HouseClearance and Removals,
Marlow Dene
LM47 2QT
Tel: 07815239604
Email: enquiries@tidynests-example.info

```html
<!DOCTYPE html>
<html lang="en">
<head>
<meta charset="utf-8">
<title>TidyNests – Business Card</title>
<link rel="stylesheet" href="https://fonts.googleapis.com/css2?family=Anton&family=Roboto+Condensed:ital,wght@1,800&display=swap">
<style>
  :root {
    --page: #ffffff;
    --board-light: #b0803f;
    --board-mid: #a57638;
    --board-dark: #946a33;
    --ink: #1d3a20;
  }
  * { box-sizing: border-box; margin: 0; padding: 0; }
  html, body { width: 1200px; height: 900px; overflow: hidden; background: var(--page); }
  .canvas { position: relative; width: 1200px; height: 900px; }

  .card {
    position: absolute;
    left: 300px;
    width: 566px;
    height: 373px;
    background: linear-gradient(160deg, var(--board-light) 0%, var(--board-mid) 55%, var(--board-dark) 100%);
    color: var(--ink);
    font-family: "Anton", "Impact", sans-serif;
    text-transform: uppercase;
    overflow: hidden;
  }
  .card--front { top: 54px; }
  .card--back { top: 477px; }

  .brand-name {
    position: absolute; left: 0; right: 0; top: 112px;
    text-align: center; font-size: 60px; line-height: 1; letter-spacing: 4px;
    font-weight: 400;
  }
  .brand-tagline {
    position: absolute; left: 0; right: 0; top: 184px;
    text-align: center; font-size: 23px; line-height: 1; letter-spacing: 1.5px;
  }
  .handling-icons {
    position: absolute; top: 252px; left: 159px;
    display: flex; gap: 7px;
  }
  .handling-icons svg { width: 57px; height: 57px; }

  .contact-line {
    position: absolute; left: 0; right: 0; top: 324px;
    text-align: center; font-size: 15px; line-height: 1; letter-spacing: 0.6px;
    display: flex; justify-content: center; align-items: center; gap: 7px;
  }
  .contact-line .sep { width: 7px; height: 7px; background: var(--ink); display: inline-block; }

  .service-box {
    position: absolute; width: 237px; height: 115px;
    border: 6px solid var(--ink);
    display: flex; align-items: center; justify-content: center;
    text-align: center; font-size: 26px; line-height: 27px; letter-spacing: 0.5px;
  }
  .service-box--free { left: 33px; top: 32px; }
  .service-box--removals { left: 295px; top: 32px; }
  .service-box--collection { left: 33px; top: 165px; }
  .service-box--delivery { left: 295px; top: 165px; }
  .service-box em { font-style: italic; }
  .mark { display: inline-block; width: 14px; height: 16px; vertical-align: -1px; margin-left: 6px; }

  .footnote {
    position: absolute; left: 48px; top: 288px;
    font-family: "Roboto Condensed", "Arial Narrow", sans-serif;
    font-style: italic; font-weight: 800; font-size: 12.5px; letter-spacing: 0.15px;
    text-transform: none; white-space: nowrap;
    display: flex; align-items: center; gap: 6px;
  }
  .footnote .mark { margin-left: 0; width: 12px; height: 13px; }
</style>
</head>
<body>
<div class="canvas">

  <section class="card card--front">
    <h1 class="brand-name">TidyNests</h1>
    <p class="brand-tagline">Home Clearence &amp; Removals</p>

    <div class="handling-icons">
      <svg viewBox="0 0 57 57" aria-label="Handle with care">
        <rect x="1.5" y="1.5" width="54" height="54" fill="none" stroke="#1d3a20" stroke-width="3"/>
        <rect x="21" y="13" width="15" height="15" fill="#1d3a20"/>
        <path d="M10 24 L14 38 L24 46 M47 24 L43 38 L33 46" fill="none" stroke="#1d3a20" stroke-width="3.5" stroke-linejoin="round"/>
      </svg>
      <svg viewBox="0 0 57 57" aria-label="This way up">
        <rect x="1.5" y="1.5" width="54" height="54" fill="none" stroke="#1d3a20" stroke-width="3"/>
        <path d="M21 42 V16 M14 22 L21 12 L28 22 M36 42 V16 M29 22 L36 12 L43 22" fill="none" stroke="#1d3a20" stroke-width="3.5"/>
        <rect x="12" y="45" width="33" height="3.5" fill="#1d3a20"/>
      </svg>
      <svg viewBox="0 0 57 57" aria-label="Fragile">
        <rect x="1.5" y="1.5" width="54" height="54" fill="none" stroke="#1d3a20" stroke-width="3"/>
        <path d="M14 12 H43 Q42 30 30 32 V44 H37 V47 H20 V44 H27 V32 Q15 30 14 12 Z" fill="#1d3a20"/>
        <path d="M26 12 L30 19 L27 24" fill="none" stroke="#a57638" stroke-width="2"/>
      </svg>
      <svg viewBox="0 0 57 57" aria-label="Keep dry">
        <rect x="1.5" y="1.5" width="54" height="54" fill="none" stroke="#1d3a20" stroke-width="3"/>
        <path d="M10 26 Q28 6 47 26 Z" fill="#1d3a20"/>
        <path d="M28.5 26 V42 Q28.5 47 24 46" fill="none" stroke="#1d3a20" stroke-width="3"/>
      </svg>
    </div>

    <p class="contact-line">
      <span>Marlow Dene LM47 2QT</span><span class="sep"></span>
      <span>07815239604</span><span class="sep"></span>
      <span>enquiries@tidynests-example.info</span>
    </p>
  </section>

  <section class="card card--back">
    <div class="service-box service-box--free"><p><em>Free</em> Clearence<br>Service</p></div>
    <div class="service-box service-box--removals"><p>Removals<br>Service</p></div>
    <div class="service-box service-box--collection">
      <p>Collection of<br>sold online<br>items<svg class="mark" viewBox="0 0 14 16"><rect x="1" y="1" width="12" height="14" fill="none" stroke="#1d3a20" stroke-width="2"/><path d="M1 1 L13 15 M13 1 L1 15" stroke="#1d3a20" stroke-width="1.6"/></svg></p>
    </div>
    <div class="service-box service-box--delivery">
      <p>Delivery of<br>purchased<br>online items<svg class="mark" viewBox="0 0 14 16"><rect x="1" y="1" width="12" height="14" fill="none" stroke="#1d3a20" stroke-width="2"/><path d="M1 1 L13 15 M13 1 L1 15" stroke="#1d3a20" stroke-width="1.6"/></svg></p>
    </div>

    <p class="footnote">
      <svg class="mark" viewBox="0 0 14 16"><rect x="1" y="1" width="12" height="14" fill="none" stroke="#1d3a20" stroke-width="2"/><path d="M1 1 L13 15 M13 1 L1 15" stroke="#1d3a20" stroke-width="1.6"/></svg>
      <span>Includes items such as motorcycles, pianos, furniture, electrical appliances, etc.</span>
    </p>

    <p class="contact-line">
      <span>Marlow Dene LM47 2QT</span><span class="sep"></span>
      <span>07815239604</span><span class="sep"></span>
      <span>enquiries@tidynests-example.info</span>
    </p>
  </section>

</div>
</body>
</html>
```